Land Buying Company Needs Letterhead for Direct Mail Marketing to Land Owners

We are looking for a professional letterhead that we will be including in our direct mail marketing. We will be sending this to land owners who may be interested in selling or purchasing land.

The letterhead needs to be editable. Headers and footers would look nice, but we are open. We would want it to include our address, website, phone, and email info. For right now the address to use for design purposes would the following:

Address: 415 Bramwell Avenue #600
Dallas, TX 75219
Website - www.quillridgeacres.example
Email - info@quillridgeacres.example
Phone - 866-402-ACRE

I have attached our logo zip file that we just had done on Pixel Guild. Let me know what questions you have, and thank you.

```html
<!DOCTYPE html>
<html lang="en">
<head>
<meta charset="UTF-8">
<title>Quill Ridge Acres Letterhead</title>
<link href="https://fonts.googleapis.com/css2?family=Lato:wght@300;700&family=Montserrat:wght@400;600&family=Great+Vibes&display=swap" rel="stylesheet">
<style>
  :root {
    --backdrop: #d9dcdf;
    --paper: #efefef;
    --paper-shade: #e6e6e6;
    --brand-green: #6a9e2a;
    --brand-dark: #3f5a26;
    --body-text: #8c8c8c;
    --ink: #1b1b1b;
    --footer-text: #3a3a3a;
    --watermark: #dddddd;
  }
  * { margin: 0; padding: 0; box-sizing: border-box; }
  html, body { width: 1200px; height: 1200px; overflow: hidden; }
  body { background: var(--backdrop); position: relative; }

  .letterhead {
    position: absolute; left: 190px; top: 20px;
    width: 820px; height: 1160px;
    background: linear-gradient(180deg, var(--paper) 0%, var(--paper-shade) 100%);
    overflow: hidden;
    font-family: "Lato", sans-serif;
    box-shadow: 0 4px 18px rgba(0,0,0,0.15);
  }

  .brand { position: absolute; left: 55px; top: 50px; display: flex; align-items: center; gap: 14px; }
  .brand-dot { width: 54px; height: 54px; border-radius: 50%; background: var(--brand-dark); }
  .brand-name {
    font-family: "Montserrat", sans-serif; font-weight: 600;
    font-size: 24px; letter-spacing: 1.5px; color: var(--brand-green); text-transform: uppercase;
  }

  .letter { position: absolute; left: 88px; top: 254px; width: 645px; font-size: 13px; line-height: 19.3px; font-weight: 300; color: var(--body-text); }
  .date { margin-bottom: 19.3px; }
  .recipient-name { color: var(--ink); font-weight: 700; }
  .recipient { margin-bottom: 38.6px; }
  .salutation { margin-bottom: 19.3px; }
  .letter p.body-copy { text-align: justify; margin-bottom: 19.3px; }
  .closing { margin-top: 48px; }
  .signature { font-family: "Great Vibes", cursive; font-size: 30px; color: var(--ink); margin-top: 4px; margin-left: 6px; line-height: 36px; }

  .watermark-circle { position: absolute; left: 450px; top: 840px; width: 422px; height: 422px; border-radius: 50%; background: var(--watermark); opacity: 0.7; }

  .footer-bar { position: absolute; left: 0; top: 1034px; width: 10px; height: 91px; background: var(--brand-green); }
  .contact { position: absolute; left: 55px; top: 1034px; font-family: "Montserrat", sans-serif; font-size: 12.5px; line-height: 16.5px; color: var(--footer-text); }
  .contact address { font-style: normal; margin-bottom: 9px; }
  .contact-line { display: flex; align-items: center; gap: 7px; }
  .contact-line svg { width: 11px; height: 11px; flex: none; }
  .contact-line.web { color: var(--brand-green); }
</style>
</head>
<body>
  <div class="letterhead">
    <div class="brand">
      <div class="brand-dot"></div>
      <div class="brand-name">Quill Ridge Acres</div>
    </div>

    <div class="watermark-circle"></div>

    <div class="letter">
      <div class="date">01 January 2050</div>
      <div class="recipient">
        <div class="recipient-name">Company (Pvt) Ltd.</div>
        <div>PO Box 3355 Mainville St</div>
        <div>Sample City Country 3355</div>
      </div>
      <div class="salutation">Dear Martin Caldwell,</div>
      <p class="body-copy">Lorem ipsum dolor sit amet, consectetuer adipiscing elit, sed diam nonummy nibh euismod tincidunt ut laoreet dolore magna aliquam erat volutpat. Ut wisi enim ad minim veniam, quis nostrud exerci tation ullamcorper suscipit lobortis nisl ut aliquip ex ea commodo consequat. Duis dolore te feugait nulla facilisi. Nam liber tempor cum soluta nobis eleifend option congue nihil imperdiet doming id quod mazim placerat facer possim assum. Lorem ipsum dolor sit amet, consectetuer adipiscing elit, sed diam nonummy nibh euismod tincidunt ut laoreet dolore magna aliquam erat volutpat. Ut wisi enim ad minim veniam, quis nostrud exerci tation ullamcorper suscipit lobortis nisl ut aliquip ex ea commodo consequat.</p>
      <p class="body-copy">Consectetuer adipiscing elit, sed diam nonummy nibh euismod tincidunt ut laoreet dolore magna aliquam erat volutpat. Ut wisi enim ad minim veniam, quis nostrud exerci tation ullamcorper suscipit lobortis nisl ut aliquip ex ea commodo consequat. Consectetuer adipiscing elit, sed diam nonummy nibh euismod tincidunt ut laoreet dolore magna aliquam erat volutpat. Ut wisi enim ad minim veniam, quis nostrud exerci tation ullamcorper suscipit lobortis nisl ut aliquip ex ea commodo consequat.</p>
      <p class="body-copy">Consectetuer adipiscing elit, sed diam nonummy nibh euismod tincidunt ut laoreet dolore magna aliquam erat volutpat. Ut wisi enim ad minim veniam, quis nostrud exerci tation ullamcorper suscipit lobortis nisl ut aliquip ex ea commodo consequat. Consectetuer adipiscing elit, sed diam nonummy nibh euismod tincidunt ut laoreet dolore magna aliquam erat volutpat. Ut wisi enim ad minim veniam, quis nostrud exerci tation ullamcorper suscipit lobortis nisl ut aliquip ex ea commodo consequat.</p>
      <div class="closing">Sincerely Yours</div>
      <div class="signature">Edward Thomas Linley</div>
    </div>

    <div class="footer-bar"></div>
    <div class="contact">
      <address>415 Bramwell Avenue #600<br>Dallas, TX 75219</address>
      <div class="contact-line">
        <svg viewBox="0 0 12 12"><path d="M3 1 L5 3.5 L4 4.8 C4.6 6 5.8 7.3 7.2 8 L8.5 7 L11 9 L9.8 11 C5.5 10.6 1.4 6.5 1 2.2 Z" fill="#6a9e2a"/></svg>
        <span>866-402-ACRE</span>
      </div>
      <div class="contact-line">
        <svg viewBox="0 0 12 12"><rect x="1" y="2.5" width="10" height="7" fill="#6a9e2a"/><path d="M1 2.5 L6 6.5 L11 2.5" stroke="#efefef" stroke-width="1" fill="none"/></svg>
        <span>info@quillridgeacres.example</span>
      </div>
      <div class="contact-line web">
        <svg viewBox="0 0 12 12"><circle cx="6" cy="6" r="5" fill="none" stroke="#6a9e2a" stroke-width="1.2"/><ellipse cx="6" cy="6" rx="2.2" ry="5" fill="none" stroke="#6a9e2a" stroke-width="1"/><path d="M1 6 H11" stroke="#6a9e2a" stroke-width="1"/></svg>
        <span>www.quillridgeacres.example</span>
      </div>
    </div>
  </div>
</body>
</html>
```